bramblewood ridge livestock company website

we would like a home page, an about us page, a page for sires, a page for dams, A sale page where we can list progreny for sale and a contact us. on the about us page we would like there to be a family picture. on the sires page we would like to have a picture of each sire, a description beside them and a link to their online profile at prairie hereford. on the dam page we would like to have a picture of each dam, aswell as a description beside them aswell as a link to the prairie hereford site. would like the website to very mobile phone friendly as expecting most traffic to be on phone. we would like the website to look and feel very mich like a farm, rustic, barbed wire and other farm feels. we would also like a frozen genetics pages where we can include pictures and descriptions of the sires and dams aswell as a price for embryos and semen. we need to website to be easy to maintain so we can update pictures and information as it changes, we would like there to be a feature so that people can sign up to be on our mailing list by giving us their mailing addess and email and full name
aswell as an area where they can send us a message to contact us.

leaving for work for 3 weeks in the canadian arctic will have limited ability to use the internet

Target Market(s)

other ranchers, farmers, cattlemen,

Industry/Entity Type

farming, agriculture, cattle

Coding

Coded - Design and coding required

Requirements
Must have
• about page, contact page, sires page, dams page, SALE page.
Nice to have
• country/farm vibe, barbed wire, wood,

```html
<!DOCTYPE html>
<html lang="en">
<head>
<meta charset="utf-8">
<title>Bramblewood Ridge Livestock Company</title>
<link href="https://fonts.googleapis.com/css2?family=Oswald:wght@400;500&family=Cinzel:wght@600;700&family=Montserrat:wght@500&family=Source+Sans+3:wght@400&display=swap" rel="stylesheet">
<style>
:root{
  --night:#1b1916;
  --gold:#b07a45;
  --gold-soft:#c28a52;
  --paper:#ece8e3;
  --card:#f3f0ec;
  --ink:#2a2622;
  --white:#ffffff;
}
*{box-sizing:border-box;margin:0;padding:0}
html,body{width:1200px;height:800px;overflow:hidden;background:var(--night)}
.page{position:relative;width:1200px;height:800px;overflow:hidden;background:var(--paper)}
.site-header{position:absolute;left:0;top:0;width:1200px;height:100px;background:var(--night)}
.brand{position:absolute;left:70px;top:32px;display:flex;align-items:center;gap:8px;font-family:'Oswald',sans-serif;font-weight:500;font-size:13px;line-height:1.15;color:var(--white);text-transform:uppercase;width:150px}
.brand-mark{width:12px;height:12px;background:var(--white);flex:none}
.main-nav{position:absolute;left:310px;top:38px;font-family:'Oswald',sans-serif;font-size:15px;letter-spacing:.5px;color:var(--white)}
.main-nav a{color:inherit;text-decoration:none;position:absolute;white-space:nowrap}
.main-nav a.active{color:var(--gold-soft)}
.main-nav a.active::after{content:"";position:absolute;left:0;right:0;top:34px;height:2px;background:var(--gold)}
.join-btn{position:absolute;left:841px;top:24px;width:203px;height:43px;border:1.5px solid var(--gold);color:var(--white);font-family:'Oswald',sans-serif;font-size:15px;letter-spacing:.8px;display:flex;align-items:center;justify-content:center}
.social{position:absolute;top:36px;width:20px;height:20px;border:2px solid var(--white);border-radius:50%}
.hero{position:absolute;left:0;top:100px;width:1200px;height:362px;
  background:
   linear-gradient(90deg,#1c1a17 0%,#1e1b18 30%,rgba(30,27,24,.3) 55%,rgba(0,0,0,0) 70%),
   radial-gradient(ellipse at 85% 30%,#c98a4a 0%,#8a5a32 30%,#3a2b1f 65%,#1f1a15 100%)}
.hero-wire{position:absolute;left:0;top:446px;width:1200px;height:12px}
.hero-line{position:absolute;left:67px;color:var(--white);white-space:nowrap}
.eyebrow{top:152px;font-family:'Montserrat',sans-serif;font-size:15px;line-height:18px;letter-spacing:5px;display:flex;align-items:center;gap:12px}
.eyebrow .rule{width:170px;height:1px;background:#c9b9a4}
.premium{top:181px;font-family:'Cinzel',serif;font-weight:700;color:var(--gold);font-size:33px;line-height:1;letter-spacing:6px}
.angus{top:200px;left:64px;font-family:'Cinzel',serif;font-weight:700;font-size:92px;line-height:1;letter-spacing:1px}
.genetics{top:290px;font-family:'Cinzel',serif;font-weight:700;color:var(--gold);font-size:40px;line-height:1;letter-spacing:8px}
.tagline{top:341px;font-family:'Montserrat',sans-serif;font-size:15px;line-height:18px;letter-spacing:3.5px}
.tagline .dot{color:var(--gold);margin:0 6px}
.hero-actions{position:absolute;left:67px;top:382px;display:flex;gap:15px}
.btn{height:41px;display:flex;align-items:center;justify-content:center;gap:12px;white-space:nowrap;font-family:'Oswald',sans-serif;font-size:17px;letter-spacing:.8px;color:var(--white)}
.btn-solid{background:var(--gold);width:160px}
.btn-ghost{border:1.5px solid var(--white);width:218px}
.cards{position:absolute;left:0;top:462px;width:1200px;height:256px;background:var(--paper)}
.card{position:absolute;top:25px;height:206px;background:var(--card);border:1px solid #ddd6cc;border-bottom:5px solid var(--gold);text-align:center}
.card-photo{height:100px;width:100%}
.card h2{font-family:'Oswald',sans-serif;font-weight:500;font-size:20px;color:var(--ink);margin-top:7px;letter-spacing:.5px;line-height:1.1}
.card p{font-family:'Source Sans 3',sans-serif;font-size:15px;color:#3a342e;margin-top:2px}
.card-btn{display:inline-flex;align-items:center;gap:8px;margin-top:9px;height:29px;padding:0 26px;border:1px solid var(--gold);font-family:'Oswald',sans-serif;font-size:14px;color:var(--ink);letter-spacing:.5px;white-space:nowrap}
.signup{position:absolute;left:0;top:718px;width:1200px;height:82px;background:linear-gradient(180deg,#2b2a27,#23221f)}
.signup h3{position:absolute;left:67px;top:17px;font-family:'Oswald',sans-serif;font-weight:400;font-size:20px;letter-spacing:1px;color:var(--white)}
.signup .divider{position:absolute;left:225px;top:20px;width:1px;height:28px;background:var(--gold)}
.signup .lede{position:absolute;left:243px;top:21px;font-family:'Oswald',sans-serif;font-size:14px;letter-spacing:.6px;color:var(--white);white-space:nowrap}
.field{position:absolute;top:15px;height:31px;background:var(--white);font-family:'Source Sans 3',sans-serif;font-size:13px;color:#444;padding:7px 11px;white-space:nowrap}
.subscribe{position:absolute;left:1048px;top:15px;width:104px;height:31px;background:var(--gold);color:var(--white);font-family:'Oswald',sans-serif;font-size:14px;letter-spacing:.5px;display:flex;align-items:center;justify-content:center}
</style>
</head>
<body>
<div class="page">
  <header class="site-header">
    <div class="brand"><span class="brand-mark"></span><span>Bramblewood Ridge Livestock Company</span></div>
    <nav class="main-nav">
      <a class="active" href="#" style="left:0">HOME</a>
      <a href="#" style="left:61px">ABOUT US</a>
      <a href="#" style="left:151px">SIRES</a>
      <a href="#" style="left:215px">DAMS</a>
      <a href="#" style="left:277px">SALE</a>
      <a href="#" style="left:334px">FROZEN GENETICS</a>
      <a href="#" style="left:467px">CONTACT</a>
    </nav>
    <div class="join-btn">JOIN OUR MAILING LIST</div>
    <span class="social" style="left:1065px" aria-label="Social link"></span>
    <span class="social" style="left:1101px" aria-label="Social link"></span>
  </header>

  <section class="hero" role="img" aria-label="Black cattle grazing in a pasture at sunset"></section>
  <svg class="hero-wire" viewBox="0 0 1200 12" preserveAspectRatio="none"><path d="M0 4 L600 8 L1200 2" fill="none" stroke="#bdb6ad" stroke-width="1.5"/></svg>

  <div class="hero-line eyebrow">WELCOME TO <span class="rule"></span></div>
  <div class="hero-line premium">PREMIUM</div>
  <div class="hero-line angus">ANGUS</div>
  <div class="hero-line genetics">GENETICS</div>
  <div class="hero-line tagline">QUALITY<span class="dot">•</span>PERFORMANCE<span class="dot">•</span>HERITAGE</div>

  <div class="hero-actions">
    <div class="btn btn-solid">VIEW SIRES
      <svg width="20" height="14" viewBox="0 0 20 14"><path d="M1 7h17M12 1l6 6-6 6" fill="none" stroke="#fff" stroke-width="2"/></svg></div>
    <div class="btn btn-ghost">VIEW SALE ANIMALS
      <svg width="20" height="14" viewBox="0 0 20 14"><path d="M1 7h17M12 1l6 6-6 6" fill="none" stroke="#fff" stroke-width="2"/></svg></div>
  </div>

  <section class="cards">
    <article class="card" style="left:65px;width:248px">
      <div class="card-photo" role="img" aria-label="Black bull standing in a green pasture" style="background:linear-gradient(180deg,#9aa38a,#6f7a4f 55%,#2a2826)"></div>
      <h2>SIRES</h2><p>Elite Genetics</p>
      <div class="card-btn">EXPLORE <svg width="15" height="10" viewBox="0 0 15 10"><path d="M1 5h12M9 1l4 4-4 4" fill="none" stroke="#2a2622" stroke-width="1.6"/></svg></div>
    </article>
    <article class="card" style="left:327px;width:265px">
      <div class="card-photo" role="img" aria-label="Black cow standing in a field" style="background:linear-gradient(180deg,#8f988c,#6d7450 55%,#2a2826)"></div>
      <h2>DAMS</h2><p>Proven Mothers</p>
      <div class="card-btn">EXPLORE <svg width="15" height="10" viewBox="0 0 15 10"><path d="M1 5h12M9 1l4 4-4 4" fill="none" stroke="#2a2622" stroke-width="1.6"/></svg></div>
    </article>
    <article class="card" style="left:607px;width:266px">
      <div class="card-photo" role="img" aria-label="Herd of cattle in a fenced pasture at sunset" style="background:linear-gradient(180deg,#d68a45,#b06a36 40%,#3b2f25)"></div>
      <h2>SALE</h2><p>Available Now</p>
      <div class="card-btn">VIEW LISTINGS <svg width="15" height="10" viewBox="0 0 15 10"><path d="M1 5h12M9 1l4 4-4 4" fill="none" stroke="#2a2622" stroke-width="1.6"/></svg></div>
    </article>
    <article class="card" style="left:888px;width:259px">
      <div class="card-photo" role="img" aria-label="Laboratory vials of frozen genetics held by a gloved hand" style="background:linear-gradient(90deg,#d9dde2,#c4cad2 60%,#3d5fa8)"></div>
      <h2>FROZEN GENETICS</h2><p>Embryos &amp; Semen</p>
      <div class="card-btn">LEARN MORE <svg width="15" height="10" viewBox="0 0 15 10"><path d="M1 5h12M9 1l4 4-4 4" fill="none" stroke="#2a2622" stroke-width="1.6"/></svg></div>
    </article>
  </section>

  <section class="signup">
    <h3>STAY CONNECTED</h3>
    <span class="divider"></span>
    <span class="lede">SIGN UP FOR UPDATES, SALES &amp; RANCH NEWS</span>
    <div class="field" style="left:545px;width:114px">Full Name</div>
    <div class="field" style="left:663px;width:129px">Email Address</div>
    <div class="field" style="left:796px;width:247px">Mailing Address</div>
    <div class="subscribe">SUBSCRIBE</div>
  </section>
</div>
</body>
</html>
```